Business Card Design for a Lending Business (Hard Money loans)

We need a business card for our Real Estate Lending business. We do hard Money loans for real estate investors. We have an existing logo we like, see attached. I'd like the business card to mostly include the logo colors, but a bright color pop of some sort would be nice to see also. Card should include Logo, Company Name, Company Address, Employee Name, Cell Phone, Main Phone, Email, Website

Industry/Entity Type

Finance / Lending

Contact Information for Business Card

Logo, Company Name, Company Address, Employee Name, Cell Phone, Main Phone, Email, Website

Requirements
Nice to have
• I'd like the business card to mostly include the logo colors, but a bright color pop of some sort would be nice to see also.

```html
<!DOCTYPE html>
<html lang="en">
<head>
<meta charset="utf-8">
<title>Harborline Lending – Business Card</title>
<link href="https://fonts.googleapis.com/css2?family=Roboto:wght@400;500;700&display=swap" rel="stylesheet">
<style>
  :root {
    --backdrop: #9cdffc;
    --card: #ffffff;
    --navy: #0b2a8c;
    --royal: #0229c0;
    --violet: #433bd8;
    --cyan: #00aedf;
    --bright: #0047ee;
    --deep: #0006a0;
    --shadow: rgba(40, 110, 150, 0.35);
  }
  * { margin: 0; padding: 0; box-sizing: border-box; }
  html, body {
    width: 1200px; height: 1200px; overflow: hidden;
    background: var(--backdrop);
    font-family: "Roboto", Arial, sans-serif;
  }
  .stage { position: relative; width: 1200px; height: 1200px; }
  .card {
    position: absolute; left: 226px; width: 748px; height: 427px;
    background: var(--card); border-radius: 25px; overflow: hidden;
    box-shadow: 8px 10px 12px var(--shadow);
  }
  .card--front { top: 128px; }
  .card--back { top: 644px; }
  .card__waves { position: absolute; inset: 0; width: 100%; height: 100%; }
  .holder { position: absolute; right: 60px; top: 48px; text-align: right; color: var(--navy); }
  .holder__name { font-weight: 500; font-size: 63px; line-height: 1; letter-spacing: 0.5px; }
  .holder__role { font-weight: 500; font-size: 26px; line-height: 1; margin-top: 10px; margin-right: 4px; letter-spacing: 0.6px; }
  .contact { position: absolute; left: 145px; top: 226px; list-style: none; color: var(--navy); }
  .contact li { font-size: 20px; line-height: 39px; font-weight: 400; }
  .brand {
    position: absolute; left: 150px; top: 128px; width: 232px;
    display: flex; flex-direction: column; align-items: center; gap: 22px;
  }
  .brand__mark { width: 114px; height: 114px; border-radius: 50%; background: var(--cyan); }
  .brand__name {
    color: var(--navy); font-weight: 700; font-size: 25px;
    letter-spacing: 1px; white-space: nowrap; line-height: 1;
  }
</style>
</head>
<body>
<main class="stage">
  <section class="card card--front">
    <svg class="card__waves" viewBox="0 0 1204 688" preserveAspectRatio="none">
      <defs>
        <linearGradient id="frontSide" x1="0" y1="0" x2="0.6" y2="1">
          <stop offset="0" stop-color="var(--royal)"/>
          <stop offset="0.45" stop-color="var(--royal)"/>
          <stop offset="0.75" stop-color="var(--violet)"/>
          <stop offset="1" stop-color="var(--violet)"/>
        </linearGradient>
        <linearGradient id="frontCorner" x1="0" y1="0" x2="1" y2="1">
          <stop offset="0" stop-color="var(--cyan)"/>
          <stop offset="0.5" stop-color="var(--royal)"/>
          <stop offset="1" stop-color="var(--deep)"/>
        </linearGradient>
      </defs>
      <path role="img" aria-label="Flowing blue wave decoration along the left edge" fill="url(#frontSide)"
        d="M0,0 L262,0 C300,65 300,120 228,192 C215,250 185,290 155,330 C60,450 40,580 212,688 L0,688 Z"/>
      <path role="img" aria-label="Blue wave decoration in the lower right corner" fill="url(#frontCorner)"
        d="M1204,516 L1204,688 L972,688 C975,640 1000,632 1030,628 C1060,560 1130,516 1204,516 Z"/>
    </svg>
    <header class="holder">
      <h1 class="holder__name">Unknown</h1>
      <p class="holder__role">Founder/Owner</p>
    </header>
    <ul class="contact">
      <li>Your Address Goes in Here</li>
      <li>Cell phone - Main phone</li>
      <li>Your email goes here</li>
      <li>You website goes here</li>
    </ul>
  </section>

  <section class="card card--back">
    <svg class="card__waves" viewBox="0 0 1204 688" preserveAspectRatio="none">
      <defs>
        <linearGradient id="backCorner" x1="0" y1="0" x2="0.3" y2="1">
          <stop offset="0" stop-color="var(--deep)"/>
          <stop offset="0.45" stop-color="var(--royal)"/>
          <stop offset="0.75" stop-color="var(--cyan)"/>
          <stop offset="1" stop-color="var(--cyan)"/>
        </linearGradient>
        <linearGradient id="backSide" x1="0" y1="0" x2="1" y2="0.8">
          <stop offset="0" stop-color="var(--cyan)"/>
          <stop offset="0.4" stop-color="var(--cyan)"/>
          <stop offset="0.65" stop-color="var(--royal)"/>
          <stop offset="1" stop-color="var(--bright)"/>
        </linearGradient>
      </defs>
      <path role="img" aria-label="Blue wave decoration in the upper left corner" fill="url(#backCorner)"
        d="M0,0 L231,0 C230,40 210,55 170,58 C140,140 70,171 0,171 Z"/>
      <path role="img" aria-label="Flowing blue wave decoration along the right edge" fill="url(#backSide)"
        d="M846,0 L1204,0 L1204,688 L721,688 C740,560 820,500 945,433 C1000,380 1050,320 1072,248 C990,170 846,130 846,0 Z"/>
    </svg>
    <div class="brand">
      <span class="brand__mark"></span>
      <span class="brand__name">Harborline Lending</span>
    </div>
  </section>
</main>
</body>
</html>
```